Medical Aesthetics business cards

Looking for a business card for my new medical aesthetics business. I am a nurse practitioner and will be administering quilen , fillers as well as providing other services

```html
<!DOCTYPE html>
<html lang="en">
<head>
<meta charset="utf-8">
<title>Lumera Clinic – Business Cards</title>
<link rel="stylesheet" href="https://fonts.googleapis.com/css2?family=Open+Sans:wght@400;700&family=Oswald:wght@300&display=swap">
<style>
  :root {
    --backdrop: #ecebe6;
    --forest-dark: #1d3a33;
    --forest-mid: #2f4f3a;
    --forest-light: #4d6b3e;
    --ink: #1f3a35;
    --ink-soft: #3f5a55;
    --paper: #f7f8f7;
    --white: #ffffff;
  }
  * { box-sizing: border-box; margin: 0; padding: 0; }
  html, body {
    width: 1200px;
    height: 900px;
    overflow: hidden;
    background: var(--backdrop);
  }
  .canvas {
    position: relative;
    width: 1200px;
    height: 900px;
  }
  .card {
    position: absolute;
    left: 280px;
    width: 640px;
    height: 366px;
    border-radius: 4px;
    overflow: hidden;
    box-shadow: 0 8px 24px rgba(0,0,0,0.18);
  }
  .card--front { top: 70px; }
  .card--back  { top: 466px; }

  .foliage-photo {
    position: absolute;
    inset: 0;
    background:
      radial-gradient(ellipse at 30% 40%, var(--forest-light) 0%, transparent 55%),
      radial-gradient(ellipse at 75% 65%, var(--forest-mid) 0%, transparent 60%),
      linear-gradient(135deg, var(--forest-mid), var(--forest-dark));
  }

  /* Front */
  .front-panel {
    position: absolute;
    top: 26px; left: 30px; right: 30px; bottom: 26px;
    background: var(--paper);
    display: flex;
    align-items: center;
  }
  .identity {
    width: 292px;
    display: flex;
    flex-direction: column;
    align-items: center;
    padding-top: 24px;
  }
  .brand {
    display: flex;
    align-items: center;
    gap: 8px;
    font-family: "Open Sans", sans-serif;
    font-weight: 700;
    font-size: 17px;
    color: var(--ink);
    margin-bottom: 16px;
  }
  .brand__dot {
    width: 12px; height: 12px;
    border-radius: 50%;
    background: var(--ink);
  }
  .person-name {
    font-family: "Open Sans", sans-serif;
    font-weight: 700;
    font-size: 28px;
    color: var(--ink);
    line-height: 1.1;
  }
  .person-role {
    font-family: "Open Sans", sans-serif;
    font-weight: 400;
    font-size: 13px;
    letter-spacing: 5px;
    color: var(--ink);
    margin-top: 6px;
  }
  .divider {
    width: 2px;
    height: 170px;
    background: var(--ink);
  }
  .contact {
    list-style: none;
    padding-left: 40px;
    font-family: "Open Sans", sans-serif;
    font-size: 13px;
    line-height: 1.7;
    color: var(--ink-soft);
    align-self: flex-start;
    margin-top: 46px;
  }

  /* Back */
  .frames {
    position: absolute;
    inset: 0;
  }
  .back-content {
    position: absolute;
    inset: 0;
    display: flex;
    flex-direction: column;
    align-items: center;
    justify-content: center;
    padding-top: 10px;
  }
  .back-brand {
    display: flex;
    align-items: center;
    gap: 10px;
    font-family: "Oswald", sans-serif;
    font-weight: 300;
    font-size: 26px;
    letter-spacing: 2px;
    color: var(--white);
    margin-bottom: 14px;
  }
  .back-brand__dot {
    width: 14px; height: 14px;
    border-radius: 50%;
    background: var(--white);
  }
  .back-title {
    font-family: "Oswald", sans-serif;
    font-weight: 300;
    font-size: 44px;
    letter-spacing: 1px;
    color: var(--white);
  }
</style>
</head>
<body>
<main class="canvas">

  <section class="card card--front">
    <div class="foliage-photo" role="img" aria-label="Dark green foliage photograph framing the card"></div>
    <div class="front-panel">
      <div class="identity">
        <div class="brand"><span class="brand__dot"></span>Lumera Clinic</div>
        <h1 class="person-name">Your Name</h1>
        <p class="person-role">NURSE PRACTITIONER</p>
      </div>
      <div class="divider"></div>
      <ul class="contact">
        <li>Email: hello@lumeraclinic.com</li>
        <li>Address: 2290 Alder Lane</li>
        <li>Phone: 008 412 730 5196</li>
      </ul>
    </div>
  </section>

  <section class="card card--back">
    <div class="foliage-photo" role="img" aria-label="Dark green close-up photograph of leaves"></div>
    <svg class="frames" width="640" height="366" viewBox="0 0 640 366" aria-hidden="true">
      <rect x="70" y="30" width="530" height="280" fill="none" stroke="#ffffff" stroke-width="4"/>
      <rect x="40" y="56" width="530" height="280" fill="none" stroke="#ffffff" stroke-width="4"/>
    </svg>
    <div class="back-content">
      <div class="back-brand"><span class="back-brand__dot"></span>Lumera Clinic</div>
      <h2 class="back-title">NURSE PRACTITIONER</h2>
    </div>
  </section>

</main>
</body>
</html>
```